Postcard: Live Ever Kinder

Text for front: HOW TO CHANGE THE WORLD IN ONE [note: the word "one" should be underlined] STEPHint: It's up to you...[Note: add arrow or something to indicate "turn over"]Text for back: You're going to spend your entire life with someone you can never get away from. (Guess who?) Wouldn't you rather that person #LiveEverKinder than judgmental or critical? BE the change you want to see! Visit www.LiveEverKinder-hub.com for daily Bright Pebbles and community. PLEASE JOIN US![Note: add logo to left half of back side]Font preference for text: Josefin sans

Target Market(s)

People who would be attracted to Calvera church - unitarian universalist message. It's spiritual without being overtly religious, so the target market is probably early 30s and up but ideally won't turn off Millennials (folks under 30). It should attract attention of people who are open-minded and committed to progressive social change, tired of an atmosphere of hate-mongering and divisiveness.

Requirements
Nice to have
• It would be nice to convey a sense of challenge - there is an idea of "bright pebbles" so something related to fire/sparks is appropriate. This is meant to evoke a deeper, divine love more than a sense of romantic love. This love is more fierce than fluffy! Yet it calls us to be our best selves.
Should not have
• Please avoid excessive pink - just the logo is enough, as this design needs to appeal to men as well as women.

```html
<!DOCTYPE html>
<html lang="en">
<head>
<meta charset="utf-8">
<title>Live Ever Kinder – Postcard</title>
<link rel="stylesheet" href="https://fonts.googleapis.com/css2?family=Bebas+Neue&family=Josefin+Sans:wght@300;400&family=Roboto+Slab:wght@500&display=swap">
<style>
  :root {
    --page: #ffffff;
    --sun: #fde16a;
    --peach: #f6b48a;
    --coral: #ee8f86;
    --rose: #e46f86;
    --magenta: #e8426f;
    --ink: #2b2b2b;
    --white: #ffffff;
    --logo-pink: #ea5b8c;
  }
  * { margin: 0; padding: 0; box-sizing: border-box; }
  html, body { width: 1200px; height: 1200px; overflow: hidden; background: var(--page); }
  .canvas { position: relative; width: 1200px; height: 1200px; }

  .card {
    position: absolute; top: 205px; width: 500px; height: 731px; overflow: hidden;
    background:
      radial-gradient(ellipse 75% 45% at 30% 38%, rgba(253,225,106,.95) 0%, rgba(253,225,106,0) 70%),
      linear-gradient(165deg, var(--peach) 0%, #f7c27a 35%, var(--peach) 60%, var(--coral) 85%, var(--rose) 100%);
  }
  .card--front { left: 80px; }
  .card--back { left: 622px; }

  .brand { position: absolute; left: 0; right: 0; top: 48px; text-align: center; }
  .brand__dot { display: block; width: 110px; height: 110px; margin: 0 auto 16px; border-radius: 50%; background: var(--logo-pink); }
  .brand__name { font-family: 'Josefin Sans', sans-serif; font-weight: 400; font-size: 26px; letter-spacing: 2px; color: var(--ink); }

  .frames { position: absolute; left: 0; top: 0; }

  .headline {
    position: absolute; left: 34px; width: 432px; top: 292px; text-align: center;
    font-family: 'Bebas Neue', sans-serif; font-weight: 400; font-size: 88px; line-height: 72px; color: var(--ink);
    letter-spacing: -2px;
  }
  .headline__line { display: block; white-space: nowrap; transform: scaleX(0.88); transform-origin: center; }
  .headline__accent { color: var(--magenta); }
  .headline__under { text-decoration: underline; text-decoration-thickness: 4px; text-underline-offset: 6px; }

  .hint {
    position: absolute; left: 36px; top: 600px;
    font-family: 'Josefin Sans', sans-serif; font-weight: 400; font-size: 35px; color: var(--magenta);
  }
  .turn-over { position: absolute; left: 160px; top: 660px; }
  .turn-over__label {
    position: absolute; left: 14px; top: 16px; white-space: nowrap;
    font-family: 'Roboto Slab', serif; font-weight: 500; font-size: 14px; color: var(--white);
    transform: rotate(-2deg);
  }

  .message {
    position: absolute; left: 20px; right: 20px; top: 270px; text-align: center;
    font-family: 'Josefin Sans', sans-serif; font-weight: 300; color: var(--ink);
    font-size: 24px; line-height: 33px;
  }
  .message__guess { display: block; font-size: 42px; line-height: 50px; color: var(--magenta); margin: 2px 0 6px; }
  .message__visit { display: block; margin-top: 14px; }
  .message__url { display: block; font-size: 34px; line-height: 40px; font-weight: 400; margin-top: 4px; }
  .message__url-name { color: var(--magenta); }
  .message__tail { display: block; line-height: 26px; }

  .join {
    position: absolute; left: 0; right: 0; top: 640px; text-align: center;
    font-family: 'Bebas Neue', sans-serif; font-size: 84px; line-height: 84px; color: var(--ink); letter-spacing: -1px;
  }
  .join__light { color: var(--white); }
</style>
</head>
<body>
<main class="canvas">

  <section class="card card--front" aria-label="Postcard front">
    <div class="brand">
      <span class="brand__dot"></span>
      <span class="brand__name">Live Ever Kinder</span>
    </div>

    <svg class="frames" width="500" height="731" viewBox="0 0 500 731" aria-hidden="true">
      <polygon points="63,243 482,298 460,587 20,530" fill="none" stroke="rgba(255,255,255,.75)" stroke-width="5"/>
      <rect x="34" y="269" width="432" height="290" fill="none" stroke="var(--magenta)" stroke-width="5"/>
    </svg>

    <h1 class="headline">
      <span class="headline__line">How to change</span>
      <span class="headline__line">the <span class="headline__accent">world</span></span>
      <span class="headline__line">in <span class="headline__under">one</span> step</span>
    </h1>

    <p class="hint">Hint: It's up to you...</p>

    <div class="turn-over">
      <svg width="300" height="70" viewBox="0 0 300 70" aria-hidden="true">
        <polygon points="0,16 270,8 272,40 0,48" fill="var(--magenta)"/>
        <path d="M250,40 C280,32 292,22 294,0 C300,20 298,45 270,52 Z" fill="#d52e6a"/>
      </svg>
      <span class="turn-over__label">SEE BACK FOR MORE DETAILS!</span>
    </div>
  </section>

  <section class="card card--back" aria-label="Postcard back">
    <div class="brand">
      <span class="brand__dot"></span>
      <span class="brand__name">Live Ever Kinder</span>
    </div>

    <p class="message">
      You're going to spend your entire life with someone you can never get away from.
      <span class="message__guess">(GUESS WHO?)</span>
      Wouldn't you rather that person #LiveEverKinder than judgmental or critical? BE the change you want to see!
      <span class="message__visit">Visit:</span>
      <span class="message__url">www.<span class="message__url-name">LiveEverKinder</span>-hub.com</span>
      <span class="message__tail">for daily Bright Pebbles and community.</span>
    </p>

    <p class="join">Please <span class="join__light">join</span> us!</p>
  </section>

</main>
</body>
</html>
```